Application Dashboard Skin - Non coded theme only

We are looking for a website color theme/look feel for a new .net dashboard application we are building. Target audience who will be using this are E and C level professionals. We are looking for the following:

Images of optional color themes for our existing dashboard. You can access a temporary version with no styling here: http://vantorquel.net:99/ . Application built in telerik and highcharts.

We are not looking for finished code or application skins. Our development team will take your final design (with specific colors/images/etc. provided) and apply it to the final beta version of the application.

Design considerations:
We are open to creative ideas, but please know that preference will be given to professional designs with emphasis on a consistent brand look/feel. Designs and colors should be focused on quickly identifying and processing the data.

Multiple submissions welcome.

-Pellowrin team

Target Market(s)

IT / Insurance

Industry/Entity Type

Building

Number of Pages Required

3 page

Requirements
Must have
• Application Dashboard link for design: http://vantorquel.net:99/

```html
<!DOCTYPE html>
<html lang="en">
<head>
<meta charset="utf-8">
<title>Claimlens – Accuracy Results</title>
<link rel="stylesheet" href="https://fonts.googleapis.com/css2?family=Open+Sans:wght@400;600;700&display=swap">
<style>
  :root{
    --orange:#f7941d;
    --ink:#222;
    --muted:#555;
    --line:#dcdcdc;
    --page:#efefef;
    --panel:#ffffff;
    --row-a:#e6e6e6;
    --row-b:#f3f3f3;
    --dark:#111;
  }
  *{box-sizing:border-box;margin:0;padding:0}
  html,body{width:792px;height:1200px;overflow:hidden}
  body{font-family:"Open Sans",Arial,sans-serif;color:var(--ink);background:var(--page)}
  .canvas{position:relative;width:792px;height:1200px;overflow:hidden;background:var(--page)}

  .topbar{position:absolute;left:0;top:0;width:792px;height:74px;background:var(--panel);border-bottom:1px solid var(--line)}
  .brand{position:absolute;left:36px;top:22px;display:flex;align-items:center;gap:6px}
  .brand-name{font-size:24px;font-weight:600;color:#333;letter-spacing:-0.5px}
  .brand-dot{width:16px;height:16px;border-radius:50%;background:var(--orange)}
  .brand-tag{position:absolute;left:131px;top:48px;font-size:8px;color:#333}
  .nav{position:absolute;top:30px;font-size:10px;color:#333}
  .nav.active{border-bottom:1.5px solid var(--orange);padding-bottom:6px}

  .panel{position:absolute;background:var(--panel);border:1px solid var(--line)}
  .panel-head{height:31px;display:flex;align-items:center;border-bottom:1px solid var(--line);padding-left:10px;font-size:10px;font-weight:600}
  .panel-head .title{flex:1}
  .select{height:21px;border:1px solid var(--line);display:flex;align-items:center;font-size:8.5px;font-weight:400;padding-left:6px;margin-right:6px}
  .select .caret{width:16px;height:100%;border-left:1px solid var(--line);margin-left:8px;position:relative}
  .select .caret::after{content:"";position:absolute;left:5px;top:8px;border:3px solid transparent;border-top:4px solid #333}
  .menu{width:30px;height:100%;border-left:1px solid var(--line);display:flex;flex-direction:column;justify-content:center;align-items:center;gap:2.5px}
  .menu i{display:block;width:12px;height:1.8px;background:#222}

  .tabs{height:30px;display:flex;align-items:center;gap:12px;padding-left:10px;border-bottom:1px solid var(--line);font-size:10px;font-weight:600}
  .tab.active{background:var(--orange);color:#fff;padding:3px 8px}
  .chart-head{height:30px;display:flex;align-items:center;border-bottom:1px solid var(--line);font-size:9px;font-weight:600}
  .chart-head .title{flex:1;text-align:center;padding-left:30px}
  .chart-head .title span{font-weight:400}
  .spacer{height:29px;border-bottom:1px solid var(--line);border-top:1px solid var(--line)}
  svg text{font-family:"Open Sans",Arial,sans-serif}

  .kpi-hero{height:66px;text-align:center;padding-top:22px}
  .kpi-hero h3{font-size:10px;font-weight:600}
  .kpi-hero p{font-size:13px;font-weight:600;color:var(--muted)}
  .kpi-row{height:28.4px;display:flex;align-items:center;padding:0 8px 0 5px;font-size:8.4px}
  .kpi-row:nth-child(odd){background:var(--row-a)}
  .kpi-row:nth-child(even){background:var(--row-b)}
  .kpi-icon{width:15px;height:15px;border-radius:50%;background:var(--orange);margin-right:12px;position:relative}
  .kpi-icon::before{content:"";position:absolute;left:4px;top:7px;width:6px;height:1.4px;background:#fff}
  .kpi-icon::after{content:"";position:absolute;left:7px;top:5px;width:3px;height:3px;border-top:1.4px solid #fff;border-right:1.4px solid #fff;transform:rotate(45deg)}
  .kpi-row .label{flex:1}

  .footer{position:absolute;left:0;top:1170px;width:792px;height:30px;background:#fff;border-top:1px solid var(--line);text-align:center;font-size:7.5px;padding-top:10px}
</style>
</head>
<body>
<div class="canvas">

  <header class="topbar">
    <div class="brand"><span class="brand-name">claimlens</span><span class="brand-dot"></span></div>
    <div class="brand-tag">Performance Insight</div>
    <span class="nav active" style="left:426px">Accuracy Results</span>
    <span class="nav" style="left:522px">Processor Accuracy</span>
    <span class="nav" style="left:630px">Manage Users</span>
    <span class="nav" style="left:716px">Settings</span>
  </header>

  <!-- Accuracy Results -->
  <section class="panel" style="left:35px;top:100px;width:450px;height:270px">
    <div class="panel-head">
      <span class="title">Accuracy Results</span>
      <span class="select">End to End<span class="caret"></span></span>
      <span class="menu"><i></i><i></i><i></i></span>
    </div>
    <svg width="448" height="238" viewBox="0 0 562 299">
      <line x1="36" y1="0" x2="36" y2="299" stroke="#dcdcdc"/>
      <text transform="translate(23 145) rotate(-90)" text-anchor="middle" font-size="11">Overall Accuracy</text>
      <text x="306" y="29" text-anchor="middle" font-size="13" font-weight="700">YTD Overall Accuracy</text>
      <text x="306" y="45" text-anchor="middle" font-size="10" fill="#555">Click the bars to view YTD details for the specific region</text>
      <g stroke="#eee">
        <line x1="77" y1="77" x2="560" y2="77"/><line x1="77" y1="113" x2="560" y2="113"/>
        <line x1="77" y1="149" x2="560" y2="149"/><line x1="77" y1="186" x2="560" y2="186"/>
        <line x1="77" y1="222" x2="560" y2="222"/>
      </g>
      <line x1="77" y1="50" x2="77" y2="258" stroke="#999"/>
      <line x1="77" y1="258" x2="560" y2="258" stroke="#ccc"/>
      <g font-size="11" text-anchor="end">
        <text x="68" y="81">100</text><text x="68" y="117">97.5</text><text x="68" y="153">95</text>
        <text x="68" y="190">92.5</text><text x="68" y="226">90</text><text x="68" y="262">87.5</text>
      </g>
      <g fill="var(--orange)">
        <rect x="122" y="105" width="31" height="153"/>
        <rect x="211" y="94" width="31" height="164"/>
        <rect x="298" y="124" width="31" height="134"/>
        <rect x="388" y="105" width="31" height="153"/>
        <rect x="484" y="152" width="31" height="106"/>
      </g>
      <g font-size="10" text-anchor="middle">
        <text x="138" y="99">97.7%</text><text x="226" y="88">98.5%</text><text x="313" y="118">96.8%</text>
        <text x="404" y="97">97.7%</text><text x="500" y="146">94.9%</text>
      </g>
      <g font-size="12" font-weight="700" text-anchor="middle">
        <text x="136" y="284">Colorado</text><text x="228" y="284">Georgia</text><text x="312" y="284">Hawaii</text>
        <text x="404" y="284">Mid Atlantic</text><text x="504" y="284">North West</text>
      </g>
    </svg>
  </section>

  <!-- Error Impact -->
  <section class="panel" style="left:35px;top:385px;width:450px;height:747px">
    <div class="panel-head">
      <span class="title">Error Impact for June 2016</span>
      <span class="select" style="margin-right:10px">End to End<span class="caret"></span></span>
    </div>
    <nav class="tabs">
      <span class="tab active">All Errors</span><span class="tab">Providers</span><span class="tab">Employers</span><span class="tab">Line Of Business</span>
    </nav>
    <div class="chart-head"><span class="title">Top 10 Error Reasons <span>(All Regions)</span></span><span class="menu"><i></i><i></i><i></i></span></div>
    <svg width="448" height="295" viewBox="0 0 562 370">
      <line x1="35" y1="0" x2="35" y2="370" stroke="#dcdcdc"/>
      <text transform="translate(22 170) rotate(-90)" text-anchor="middle" font-size="11">All Errors</text>
      <g stroke="#eee"><line x1="300" y1="28" x2="300" y2="295"/><line x1="369" y1="28" x2="369" y2="295"/><line x1="438" y1="28" x2="438" y2="295"/><line x1="508" y1="28" x2="508" y2="295"/></g>
      <line x1="229" y1="28" x2="229" y2="295" stroke="#999"/>
      <g font-size="11">
        <text x="61" y="44">Incorrect Contract/Fee</text><text x="61" y="72">Claim Paid Incorrectly</text>
        <text x="61" y="101">Not a Halvern Benefit Bill Medi</text><text x="61" y="126">Incorrect Co-Pay/Coins</text>
        <text x="59" y="152">Copay Amount not Correct</text><text x="59" y="178">Did not Follow PNP</text>
        <text x="59" y="202">Did not Follow Desk Proj</text><text x="59" y="228">Claim Denied in Error</text>
        <text x="60" y="253">Unknown</text><text x="59" y="278">Denied Incorrectly-Auth</text>
      </g>
      <g fill="var(--orange)">
        <rect x="231" y="36" width="249" height="11"/><rect x="231" y="63" width="193" height="11"/>
        <rect x="231" y="90" width="186" height="11"/><rect x="231" y="116" width="180" height="11"/>
        <rect x="231" y="142" width="140" height="11"/><rect x="231" y="169" width="140" height="11"/>
        <rect x="231" y="194" width="136" height="11"/><rect x="231" y="220" width="95" height="11"/>
        <rect x="231" y="245" width="95" height="11"/><rect x="231" y="270" width="87" height="11"/>
      </g>
      <g font-size="11">
        <text x="487" y="46">35</text><text x="430" y="72">26</text><text x="423" y="99">24</text><text x="420" y="125">23</text>
        <text x="377" y="151">20</text><text x="377" y="178">20</text><text x="374" y="203">19</text><text x="330" y="229">14</text>
        <text x="330" y="254">14</text><text x="324" y="279">12</text>
      </g>
      <g font-size="11" text-anchor="middle"><text x="231" y="311">0</text><text x="298" y="312">10</text><text x="370" y="312">20</text><text x="444" y="313">30</text><text x="508" y="314">40</text></g>
      <text x="352" y="350" text-anchor="middle" font-size="15" font-weight="700">Count</text>
    </svg>
    <div class="spacer"></div>
    <div class="chart-head"><span class="title">Top 10 Error Reasons <span>(Financial Impact,All Regions)</span></span><span class="menu"><i></i><i></i><i></i></span></div>
    <svg width="448" height="300" viewBox="0 0 562 377">
      <line x1="35" y1="0" x2="35" y2="377" stroke="#dcdcdc"/>
      <text transform="translate(22 175) rotate(-90)" text-anchor="middle" font-size="11">All Errors</text>
      <line x1="226" y1="40" x2="226" y2="296" stroke="#999"/>
      <g font-size="11">
        <text x="57" y="54">Incorrect Contract/Fee</text><text x="57" y="83">Claim Paid Incorrectly</text>
        <text x="57" y="112">Not a Halvern Benefit Bill Medi</text><text x="57" y="137">Incorrect Co-Pay/Coins</text>
        <text x="55" y="163">Copay Amount not Correct</text><text x="55" y="189">Did not Follow PNP</text>
        <text x="55" y="213">Did not Follow Desk Proj</text><text x="54" y="239">Claim Denied in Error</text>
        <text x="55" y="264">Unknown</text><text x="55" y="289">Denied Incorrectly-Auth</text>
      </g>
      <g fill="var(--orange)">
        <rect x="286" y="44" width="201" height="12"/><rect x="393" y="71" width="76" height="12"/>
        <rect x="438" y="125" width="17" height="12"/><rect x="379" y="204" width="93" height="12"/>
        <rect x="454" y="230" width="23" height="12"/><rect x="454" y="280" width="5" height="12"/>
      </g>
      <g font-size="9.5">
        <text x="229" y="54">$ -65155.67</text><text x="494" y="53">$ -12510.63</text>
        <text x="475" y="80">$ -2919.39</text>
        <text x="420" y="107">$ -245</text><text x="460" y="107">$ 0</text>
        <text x="386" y="134">$ -3898.21</text><text x="460" y="134">$ 693.01</text>
        <text x="421" y="165">$ -295</text><text x="460" y="165">$ 10</text>
        <text x="435" y="190">$ 0</text><text x="460" y="190">$ 0</text>
        <text x="321" y="214">$ -29341.33</text><text x="477" y="213">$ 10390.26</text>
        <text x="436" y="240">$ 0</text>
        <text x="436" y="264">$ 0</text><text x="460" y="264">$ 331.1</text>
        <text x="418" y="290">$ -1.81</text><text x="466" y="290">$ 1805.56</text>
      </g>
      <g font-size="11" text-anchor="middle"><text x="240" y="318">- 80</text><text x="295" y="318">- 60</text><text x="349" y="318">- 40</text><text x="403" y="318">- 20</text><text x="454" y="318">0K</text><text x="509" y="318">20K</text></g>
      <text x="358" y="357" text-anchor="middle" font-size="15" font-weight="700">$ Amount</text>
    </svg>
  </section>

  <!-- KPIs -->
  <aside class="panel" style="left:531px;top:100px;width:221px;height:462px">
    <div class="panel-head" style="padding-left:11px">
      <span class="title">KPI's</span>
      <span class="select">All Regions<span class="caret"></span></span>
    </div>
    <div class="kpi-hero"><h3>YTD Overall Accuracy</h3><p>97.41%</p></div>
    <div class="kpi-list">
      <div class="kpi-row"><span class="kpi-icon"></span><span class="label">Claims Audited:</span>4859</div>
      <div class="kpi-row"><span class="kpi-icon"></span><span class="label">Avg. Claims Audited per day</span>6.7</div>
      <div class="kpi-row"><span class="kpi-icon"></span><span class="label">Errors Found:</span>2147</div>
      <div class="kpi-row"><span class="kpi-icon"></span><span class="label">Financial Impact:</span>$1,462,139</div>
      <div class="kpi-row"><span class="kpi-icon"></span><span class="label">Total Claims Posted</span>17,773,591</div>
      <div class="kpi-row"><span class="kpi-icon"></span><span class="label">Total Encounter Claims:</span>93,984,586</div>
      <div class="kpi-row"><span class="kpi-icon"></span><span class="label">Total Auto Adjudication Claim Count:</span>920,918</div>
      <div class="kpi-row"><span class="kpi-icon"></span><span class="label">Total Adjustment Claim Count:</span>920,918</div>
      <div class="kpi-row"><span class="kpi-icon"></span><span class="label">Total Denied Claim Count:</span>133,523</div>
      <div class="kpi-row"><span class="kpi-icon"></span><span class="label">Total Dollars Paid:</span>$5,669,835,044</div>
      <div class="kpi-row"><span class="kpi-icon"></span><span class="label">Auto Adjudication Rate:</span>$0.052</div>
      <div class="kpi-row"><span class="kpi-icon"></span><span class="label">Adjustment Rate:</span>1.345%</div>
      <div class="kpi-row"><span class="kpi-icon"></span><span class="label">Denial Rate:</span>0.751%</div>
    </div>
  </aside>

  <!-- Paid vs Denied -->
  <section class="panel" style="left:531px;top:574px;width:221px;height:224px">
    <div class="panel-head" style="padding-left:12px;font-size:11px">
      <span class="title">Paid vs. Denied</span>
      <span class="menu"><i></i><i></i><i></i></span>
    </div>
    <svg width="219" height="191" viewBox="0 0 274 239">
      <circle cx="128" cy="113" r="67" fill="none" stroke="var(--orange)" stroke-width="35"/>
      <circle cx="128" cy="113" r="67" fill="none" stroke="var(--dark)" stroke-width="35" stroke-dasharray="6 415" transform="rotate(-90 128 113)" />
      <path d="M158 20 L145 20" stroke="#000" stroke-width="1.5"/><path d="M145 20 l6 -4 l0 8z"/>
      <text x="163" y="23" font-size="10">Denied: 0.7</text>
      <path d="M150 209 L138 203" stroke="#000" stroke-width="1.5"/><path d="M136 201 l7 0 l-3 6z"/>
      <text x="155" y="212" font-size="10">Paid: 99.3%</text>
    </svg>
  </section>

  <!-- Paid vs Encounter -->
  <section class="panel" style="left:531px;top:812px;width:221px;height:228px">
    <div class="panel-head" style="padding-left:12px;font-size:11px">
      <span class="title">Paid vs. Encounter</span>
      <span class="menu"><i></i><i></i><i></i></span>
    </div>
    <svg width="219" height="195" viewBox="0 0 274 244">
      <circle cx="128" cy="128" r="67" fill="none" stroke="var(--orange)" stroke-width="35"/>
      <circle cx="128" cy="128" r="67" fill="none" stroke="var(--dark)" stroke-width="35" stroke-dasharray="34 387" transform="rotate(-98 128 128)" />
      <path d="M172 40 L160 42" stroke="#000" stroke-width="1.5"/><path d="M158 42 l6 -5 l1 8z"/>
      <text x="176" y="43" font-size="10">Paid: 15.9%</text>
      <path d="M160 227 L148 221" stroke="#000" stroke-width="1.5"/><path d="M146 219 l7 0 l-3 6z"/>
      <text x="164" y="230" font-size="10">Encounter: 84.1%</text>
    </svg>
  </section>

  <footer class="footer">© 2016 CLAIMLENS All Right Reserved.</footer>
</div>
</body>
</html>
```